Creative, fresh business card design for Orrin Linings

We need a fresh, creative business card design for Orrin Linings. We are the manufacturer of Orrin Linings in Australia. Wall panels are 2400 x 1200mm panels made from MDF and feature 3D patterns on the face of the panel. The colours to be used are green, silver/grey and white RGB
Red 187
Green 207
Blue 65.

An idea is to possibly use a watermark of one of our designs as a background (like on the "Ferns" design on the left hand side of page 2 of our brochure).

Target Market(s)

Interior designers, architects, builders and home renovators

Industry/Entity Type

Business

Contact Information for Business Card

Details to go on the card are:
Our logo (attached),
Slogan: "Decorative panels for interiors and exteriors",
Contact name,
Position,
Mobile phone number,
Business address,
Business phone,
Business fax,
Website and
Email address.

I have attached a few images of our panels and our brochure for reference.

The colours of the business card should feature our logo colours which are: RGB
Red 187
Green 207
Blue 65

Requirements
Must have
• Very modern fonts and design. Some of the designs shown especially the "Weave" design which is a popular design.
Nice to have
• Creative but simple design. Very contemporary.
Should not have
• Anything ornate or old fashioned.

```html
<!DOCTYPE html>
<html lang="en">
<head>
<meta charset="utf-8">
<title>Orrin Linings – Business Card</title>
<link href="https://fonts.googleapis.com/css2?family=Questrial&display=swap" rel="stylesheet">
<style>
  :root {
    --canvas: #e9e7e3;
    --card-black: #141414;
    --card-dark: #1f1f1f;
    --brand-green: rgb(187, 207, 65);
    --silver: #a7a9ac;
    --text-light: #d9d9d9;
    --text-muted: #9a9a9a;
  }
  * { margin: 0; padding: 0; box-sizing: border-box; }
  html, body {
    width: 1200px; height: 1022px; overflow: hidden;
    background: var(--canvas);
    font-family: "Questrial", "Century Gothic", sans-serif;
  }
  .stage {
    width: 1200px; height: 1022px;
    display: flex; align-items: center; justify-content: center;
  }
  .card {
    position: relative;
    width: 1000px; height: 572px;
    overflow: hidden;
    box-shadow: 0 18px 40px rgba(0,0,0,.35);
  }
  .card__texture {
    position: absolute; inset: 0;
    background: radial-gradient(ellipse at 35% 30%, var(--card-dark) 0%, var(--card-black) 70%);
  }
  .brand {
    position: absolute; left: 52px; top: 238px;
  }
  .brand__row { display: flex; align-items: center; gap: 14px; }
  .brand__square { width: 42px; height: 42px; background: var(--brand-green); }
  .brand__name { color: var(--brand-green); font-size: 34px; line-height: 1; }
  .brand__slogan {
    margin-top: 12px; color: var(--text-muted);
    font-size: 15px; letter-spacing: 2.2px; line-height: 1.35;
  }
  .address {
    position: absolute; left: 350px; top: 218px;
    color: var(--text-muted); font-size: 26px; line-height: 1.4; letter-spacing: 1px;
  }
  .person {
    position: absolute; right: 52px; top: 88px; text-align: right;
  }
  .person__name { color: var(--brand-green); font-size: 46px; letter-spacing: 1px; }
  .person__role { color: var(--text-muted); font-size: 24px; letter-spacing: 2px; margin-top: 4px; }
  .divider {
    position: absolute; left: 340px; right: 26px; top: 305px;
    height: 2px; background: var(--brand-green);
  }
  .contacts {
    position: absolute; left: 340px; top: 326px; list-style: none;
  }
  .contacts li {
    display: flex; align-items: center; gap: 14px;
    height: 38px; color: var(--text-light); font-size: 26px; letter-spacing: 2px;
  }
  .contacts svg { width: 22px; height: 22px; flex: none; }
  .edge {
    position: absolute; left: 0; right: 0; bottom: 0; height: 30px; display: flex;
  }
  .edge__silver { flex: 0 0 72%; background: var(--silver); }
  .edge__green { flex: 1; background: var(--brand-green); }
</style>
</head>
<body>
<main class="stage">
  <article class="card">
    <div class="card__texture" role="img" aria-label="Faint embossed panel pattern on black background"></div>

    <div class="brand">
      <div class="brand__row">
        <span class="brand__square"></span>
        <span class="brand__name">Orrin Linings</span>
      </div>
      <p class="brand__slogan">decorative panels for<br>interiors &amp; landscapes</p>
    </div>

    <p class="address">4127 Harbour Lane<br>Brookvale, NSW 2100</p>

    <div class="person">
      <p class="person__name">Dale Hargrove</p>
      <p class="person__role">President</p>
    </div>

    <div class="divider"></div>

    <ul class="contacts">
      <li>
        <svg viewBox="0 0 24 24" fill="none" stroke="rgb(187,207,65)" stroke-width="2"><rect x="7" y="2" width="10" height="20" rx="2"/><line x1="11" y1="18" x2="13" y2="18"/></svg>
        0412. 618. 305
      </li>
      <li>
        <svg viewBox="0 0 24 24" fill="rgb(187,207,65)"><path d="M6.6 10.8a15 15 0 0 0 6.6 6.6l2.2-2.2a1 1 0 0 1 1-.25 11.4 11.4 0 0 0 3.6.57 1 1 0 0 1 1 1V20a1 1 0 0 1-1 1A17 17 0 0 1 3 4a1 1 0 0 1 1-1h3.5a1 1 0 0 1 1 1c0 1.25.2 2.45.57 3.6a1 1 0 0 1-.25 1z"/></svg>
        02. 9938. 4410
      </li>
      <li>
        <svg viewBox="0 0 24 24" fill="rgb(187,207,65)"><rect x="6" y="2" width="12" height="6"/><rect x="2" y="9" width="20" height="9" rx="1"/><rect x="6" y="15" width="12" height="7" fill="#141414" stroke="rgb(187,207,65)" stroke-width="2"/></svg>
        02. 9938. 4411
      </li>
      <li>
        <svg viewBox="0 0 24 24" fill="rgb(187,207,65)"><rect x="2" y="5" width="20" height="14"/><path d="M2 5l10 8 10-8" fill="none" stroke="#141414" stroke-width="2"/></svg>
        dale@orrinlinings.com
      </li>
      <li>
        <svg viewBox="0 0 24 24" fill="none" stroke="rgb(187,207,65)" stroke-width="2"><circle cx="12" cy="12" r="9"/><ellipse cx="12" cy="12" rx="4" ry="9"/><line x1="3" y1="12" x2="21" y2="12"/></svg>
        www.orrinlinings.com
      </li>
    </ul>

    <div class="edge">
      <span class="edge__silver"></span>
      <span class="edge__green"></span>
    </div>
  </article>
</main>
</body>
</html>
```